PETAL Project Roll Up Banner 85x200 cm (1:10, 1200 dpi)

PETAL is a EU-funded project to promote female entrepreneurship networks. The project is developed by 9 partners from 7 different countries.
The banner is to be used throughout the project in exhibitions, conferences, roundtables, etc.
It has to include the following graphic elements, which cannot be modified beyond scaling:
- PETAL logo
- EU logo (cannot be modified in any way, and cannot have any kind of background, but pure white).
- 9 partners logos
- Friendlane link (with logo)
- Workmesh link (with logo)
- Project's website (www.petal-circlehub.eu)
The text to be included:
Pioneering Enterprising Talent And Leadership
PETAL: Contributes to the strengthening of the links between women entrepreneurs and the mainstream of new technologies, educational, and training practices offered all over Europe.
GOOD PRACTICES: Compilation of EU projects promoting female entrepreneurship and ICT systems for learning, supporting, and training women entrepreneurs.
NETWORK: Strengthening of linkages between EU women entrepreneurs, project managers, learning communities, multipliers, and society to encourage a knowledge-sharing environment through the creation of the PETAL network.
ONE-STOP SHOP: Development of a multi-lingual EU online platform, where valuable an innovative EU learning opportunities can be found and accessed at one single place, as well as fostering new business opportunities by a Virtual Market.
The banner has to be attractive the modern female entrepreneur. It has to be easy to read, and present a fresh and exciting identity.
The banner has to include 5 additional centimetres on the top, and 10 on the bottom.
The last partner logo has been uploaded now.
Female entrepreneurs
Higher Educational Institutions
Government Female Representatives
Environment

```html
<!DOCTYPE html>
<html lang="en">
<head>
<meta charset="utf-8">
<title>PETAL Roll Up Banner</title>
<link rel="stylesheet" href="https://fonts.googleapis.com/css2?family=Advent+Pro:wght@400;500&family=Open+Sans:wght@400;600&display=swap">
<style>
  :root {
    --orange: #f7941d;
    --white: #ffffff;
    --violet: #3b2a78;
    --grey: #555a60;
    --rule: #d9d9d9;
    --badge: #e6e3ea;
  }
  * { margin: 0; padding: 0; box-sizing: border-box; }
  html, body { width: 1200px; height: 3025px; overflow: hidden; background: var(--white); }
  .banner { position: relative; width: 1200px; height: 3025px; background: var(--orange); overflow: hidden; }

  .top-margin { position: absolute; left: 0; top: 0; width: 1200px; height: 45px; background: var(--orange); }

  .hero {
    position: absolute; left: 0; top: 45px; width: 1200px; height: 1465px;
    background:
      linear-gradient(180deg, rgba(255,255,255,0) 66%, rgba(255,255,255,0.9) 84%, var(--white) 100%),
      linear-gradient(100deg, #e9ebee 0%, #cfd3d8 30%, #b9a08c 55%, #d39b78 72%, #efe3da 100%);
  }

  .brand {
    position: absolute; left: 88px; top: 1320px;
    display: flex; align-items: center; gap: 26px;
    font-family: "Advent Pro", sans-serif; font-weight: 500;
    font-size: 140px; line-height: 1; color: var(--violet); letter-spacing: 4px;
  }
  .brand-dot { width: 66px; height: 66px; border-radius: 50%; background: var(--violet); }

  .headline {
    position: absolute; left: 50px; top: 1548px; width: 1100px;
    font-family: "Advent Pro", sans-serif; font-weight: 400;
    font-size: 74px; line-height: 67px; color: var(--white); text-align: center;
  }

  .pillar { position: absolute; left: 0; width: 1200px; color: var(--white); }
  .pillar-label {
    position: absolute; left: 50px;
    font-family: "Advent Pro", sans-serif; font-weight: 400;
    font-size: 48px; line-height: 54px; text-transform: uppercase;
  }
  .pillar-text {
    position: absolute; left: 320px; width: 850px;
    font-family: "Open Sans", sans-serif; font-weight: 400;
    font-size: 29px; line-height: 43px;
  }

  .partners {
    position: absolute; left: 0; top: 2548px; width: 1200px; height: 224px;
    background: var(--white);
    display: grid; grid-template-rows: 1fr 1fr; padding: 18px 30px; row-gap: 12px;
  }
  .partner-row { display: flex; align-items: center; justify-content: space-around; }
  .partner-badge { height: 70px; background: var(--badge); border-radius: 6px; }
  .partner-badge.eu { background: var(--white); border: 3px solid var(--rule); border-radius: 0; }
  .partner-divider { width: 2px; height: 70px; background: var(--rule); }

  .footer-rule { position: absolute; left: 0; top: 2772px; width: 1200px; height: 12px; background: var(--orange); }
  .footer {
    position: absolute; left: 0; top: 2784px; width: 1200px; height: 92px;
    background: var(--white);
    display: flex; align-items: center; justify-content: space-between; padding: 0 30px;
    font-family: "Open Sans", sans-serif; font-size: 23px; color: var(--grey);
    white-space: nowrap;
  }
  .footer-item { display: flex; align-items: center; gap: 12px; }
  .footer-mark { width: 28px; height: 28px; border-radius: 50%; background: var(--grey); flex: none; }
  .footer-icon { width: 30px; height: 30px; flex: none; }
  .bottom-margin { position: absolute; left: 0; top: 2876px; width: 1200px; height: 149px; background: var(--orange); }
</style>
</head>
<body>
<main class="banner">
  <div class="top-margin"></div>

  <div class="hero" role="img" aria-label="Photograph of a female entrepreneur with a technology-themed overlay"></div>

  <div class="brand"><span class="brand-dot"></span>PETAL</div>

  <h1 class="headline">Pioneering Enterprising Talent And Leadership</h1>

  <section class="pillar" style="top:1797px">
    <h2 class="pillar-label" style="top:40px">PETAL</h2>
    <p class="pillar-text">Contributes to the strengthening of the links between women entrepreneurs and the mainstream of new technologies, educational, and training practices offered all over Europe.</p>
  </section>

  <section class="pillar" style="top:1968px">
    <h2 class="pillar-label" style="top:14px">Good<br>Practices</h2>
    <p class="pillar-text">Compilation of EU projects promoting female entrepreneurship and ICT systems for learning, supporting, and training women entrepreneurs.</p>
  </section>

  <section class="pillar" style="top:2140px">
    <h2 class="pillar-label" style="top:60px">Network</h2>
    <p class="pillar-text">Strengthening of linkages between EU women entrepreneurs, project managers, learning communities, multipliers, and society to encourage a knowledge-sharing environment through the creation of the PETAL network.</p>
  </section>

  <section class="pillar" style="top:2340px">
    <h2 class="pillar-label" style="top:18px">One-Stop<br>Shop</h2>
    <p class="pillar-text">Development of a multi-lingual EU online platform, where valuable an innovative EU learning opportunities can be found and accessed at one single place, as well as fostering new business opportunities by a Virtual Market.</p>
  </section>

  <section class="partners" aria-label="Project partners">
    <div class="partner-row">
      <div class="partner-badge" style="width:230px"></div>
      <div class="partner-divider"></div>
      <div class="partner-badge" style="width:120px"></div>
      <div class="partner-divider"></div>
      <div class="partner-badge" style="width:260px"></div>
      <div class="partner-divider"></div>
      <div class="partner-badge" style="width:280px"></div>
    </div>
    <div class="partner-row">
      <div class="partner-badge" style="width:170px"></div>
      <div class="partner-divider"></div>
      <div class="partner-badge" style="width:170px"></div>
      <div class="partner-divider"></div>
      <div class="partner-badge" style="width:200px"></div>
      <div class="partner-divider"></div>
      <div class="partner-badge" style="width:170px"></div>
      <div class="partner-divider"></div>
      <div class="partner-badge eu" style="width:160px"></div>
    </div>
  </section>

  <div class="footer-rule"></div>
  <footer class="footer">
    <div class="footer-item"><span class="footer-mark"></span>Friendlane /petal.circle</div>
    <div class="footer-item">
      <svg class="footer-icon" viewBox="0 0 34 34" aria-hidden="true">
        <circle cx="17" cy="17" r="14" fill="none" stroke="#555a60" stroke-width="2.5"/>
        <ellipse cx="17" cy="17" rx="6" ry="14" fill="none" stroke="#555a60" stroke-width="2"/>
        <line x1="3" y1="17" x2="31" y2="17" stroke="#555a60" stroke-width="2"/>
      </svg>
      www.petal-circlehub.eu
    </div>
    <div class="footer-item"><span class="footer-mark"></span>Workmesh /groups/PETALCIRCLE-4471208</div>
  </footer>
  <div class="bottom-margin"></div>
</main>
</body>
</html>
```